Sports / Entertainment Media Co needs a biz card design

We are a media co / luxury lifestyle brand that targets professional athletes, entertainers and high net-worth fans. We are currently preparing for a relaunch and in need for new biz cards. I envision a black on black card with a pop of color on opposite side. Color Palette black, white, red etc. I want this card to exude sexiness and power. Very high stylized, hip and cool. I have attached the logo - I would like to see it all in black, but also open to other ideas. I will also upload a current card with all information needed on this new card. Furthermore I will add some samples of other cards I love. Thanks!!!

I provided suggestions, however I am open to all ideas!!   Be as creative as you can.  Think cutting-edge, sexy and powerful.  Take a look at the cards I uploaded to get a sense for what I like.  Thanks!!!

Entertainment

```html
<!DOCTYPE html>
<html lang="en">
<head>
<meta charset="UTF-8">
<title>Stride — Business Card</title>
<link href="https://fonts.googleapis.com/css2?family=Open+Sans:wght@400;600;700&display=swap" rel="stylesheet">
<style>
  :root {
    --stage: #2e2e2e;
    --card-white: #ffffff;
    --card-black: #1c1c1c;
    --map-light: #3a3a3a;
    --map-dark: #222222;
    --ink: #111111;
    --ink-soft: #4a4a4a;
    --rule: #6b6b6b;
    --accent: #d81e1e;
  }
  * { box-sizing: border-box; margin: 0; padding: 0; }
  html, body { width: 1200px; height: 964px; overflow: hidden; }
  body {
    background: var(--stage);
    font-family: "Open Sans", Arial, sans-serif;
    color: var(--ink);
    display: flex;
    flex-direction: column;
    align-items: center;
    justify-content: center;
    gap: 40px;
  }
  .card {
    width: 760px;
    height: 434px;
    position: relative;
    border-radius: 4px;
    overflow: hidden;
    box-shadow: 0 10px 30px rgba(0,0,0,0.45);
  }
  .card--front { background: var(--card-white); }
  .card--back { background: var(--card-black); }

  .brand {
    position: absolute;
    left: 56px;
    top: 190px;
    display: flex;
    align-items: center;
    gap: 10px;
  }
  .brand__name {
    font-weight: 700;
    font-size: 76px;
    line-height: 1;
    letter-spacing: -2px;
    color: var(--ink);
  }
  .brand__dot {
    width: 18px; height: 18px;
    border-radius: 50%;
    background: var(--accent);
    margin-top: 30px;
  }

  .divider {
    position: absolute;
    left: 420px;
    top: 110px;
    width: 2px;
    height: 160px;
    background: var(--rule);
  }

  .contact {
    position: absolute;
    left: 446px;
    top: 104px;
  }
  .contact__name {
    font-weight: 700;
    font-size: 24px;
    letter-spacing: 0.5px;
    line-height: 1.1;
  }
  .contact__role {
    font-size: 16px;
    color: var(--ink-soft);
    letter-spacing: 0.5px;
    margin-left: 12px;
    margin-bottom: 16px;
  }
  .contact__row {
    display: flex;
    align-items: center;
    gap: 12px;
    margin-left: 26px;
    margin-bottom: 10px;
  }
  .contact__icon {
    width: 34px; height: 34px;
    border-radius: 50%;
    background: var(--ink);
    display: flex;
    align-items: center;
    justify-content: center;
    flex-shrink: 0;
  }
  .contact__lines {
    font-size: 15px;
    line-height: 1.2;
    color: var(--ink-soft);
  }

  .address {
    position: absolute;
    left: 0; right: 0;
    bottom: 46px;
    text-align: center;
    padding-left: 120px;
    font-size: 17px;
    color: var(--ink-soft);
  }

  .world-map {
    position: absolute;
    inset: 0;
    background: radial-gradient(ellipse at 55% 45%, var(--map-light) 0%, var(--map-dark) 70%);
  }
</style>
</head>
<body>
  <section class="card card--front">
    <div class="brand">
      <span class="brand__name">stride</span>
      <span class="brand__dot"></span>
    </div>

    <div class="divider"></div>

    <div class="contact">
      <p class="contact__name">DANIEL REYES</p>
      <p class="contact__role">GENERAL MANAGER</p>

      <div class="contact__row">
        <span class="contact__icon">
          <svg width="18" height="18" viewBox="0 0 24 24" aria-hidden="true">
            <path fill="#fff" d="M6.6 10.8a15.1 15.1 0 0 0 6.6 6.6l2.2-2.2c.3-.3.7-.4 1-.2 1.1.4 2.3.6 3.6.6.6 0 1 .4 1 1V20c0 .6-.4 1-1 1A17 17 0 0 1 3 4c0-.6.4-1 1-1h3.5c.6 0 1 .4 1 1 0 1.3.2 2.5.6 3.6.1.3 0 .7-.2 1z"/>
          </svg>
        </span>
        <p class="contact__lines">014 220 5381<br>014 220 5382</p>
      </div>

      <div class="contact__row">
        <span class="contact__icon">
          <svg width="18" height="18" viewBox="0 0 24 24" aria-hidden="true">
            <rect x="3" y="4" width="18" height="12" rx="1" fill="none" stroke="#fff" stroke-width="2"/>
            <rect x="9" y="18" width="6" height="2" fill="#fff"/>
          </svg>
        </span>
        <p class="contact__lines">daniel@stridemedia.co<br>www.stridemedia.co</p>
      </div>
    </div>

    <p class="address">42 Harbor Lane, 2nd floor, Suite 7B</p>
  </section>

  <section class="card card--back">
    <div class="world-map" role="img" aria-label="Faint grey world map across the dark card back"></div>
  </section>
</body>
</html>
```